Brochure Design Project

Our company is TEM Bexley Fold. (no LOGO)

We are a restaurant marketing and advertising service. We market restaurants menus by producing a menu guide, distributing flyers and post cards, and also placing the restaurants menu on our website for delivery.

We make restaurants more profitable, by making their food more accessible. Marketing restaurants on search engines, websites, friendloop, vrop, zindle, and a total of 21 different marketing techniques that make restaurants more money.

Key Point: This is all done at NO COST to the restaurant.

We are looking for a design for a brochure that will be mailed as well as handed to restaurateurs.

In my attached file I am including our sales letter. The letter can stay in letter form for the inside of a tri-fold brochure or it can be part of your design.

For more information about our service, please read the attached sales letter.

Target Market(s)

Restaurant Owners and General managers

Industry/Entity Type

Advertising

Requirements
Must have
• Must look attractive and Eye-catching

```html
<!DOCTYPE html>
<html lang="en">
<head>
<meta charset="utf-8">
<title>TEM Bexley Fold – Tri-fold Brochure Outside</title>
<link href="https://fonts.googleapis.com/css2?family=Arimo:wght@400;700&family=Bowlby+One+SC&display=swap" rel="stylesheet">
<style>
  :root {
    --page-bg: #3f6fae;
    --panel-grey: #d4d0ca;
    --panel-white: #f7f7f5;
    --panel-black: #0c0c0c;
    --cyan: #5bc2cf;
    --ink: #111111;
    --white: #ffffff;
    --tan: #bfb3a2;
  }
  * { box-sizing: border-box; margin: 0; padding: 0; }
  html, body { width: 1200px; height: 1031px; overflow: hidden; }
  body {
    background: var(--page-bg);
    font-family: "Arimo", Arial, sans-serif;
    position: relative;
  }
  .brochure {
    position: absolute;
    left: 53px; top: 100px;
    width: 1093px; height: 848px;
    display: flex;
    box-shadow: 0 4px 18px rgba(0,0,0,.35);
  }
  .panel { position: relative; height: 100%; overflow: hidden; }

  /* Left panel */
  .panel--intro { width: 367px; background: var(--panel-grey); }
  .intro__arrow { position: absolute; left: 100px; top: 50px; }
  .intro__site-vertical {
    position: absolute;
    left: -6px; top: 740px;
    transform: rotate(-90deg);
    transform-origin: left top;
    font-family: "Bowlby One SC", sans-serif;
    font-size: 44px;
    color: transparent;
    -webkit-text-stroke: 1.3px var(--white);
    white-space: nowrap;
    letter-spacing: 1px;
  }
  .intro__title {
    position: absolute; left: 68px; top: 112px; width: 290px;
    font-family: "Bowlby One SC", sans-serif;
    font-size: 28px; line-height: 33px;
    color: var(--ink);
    font-weight: 400;
  }
  .intro__body {
    position: absolute; left: 68px; top: 272px; width: 285px;
    font-size: 13.5px; line-height: 19.5px; color: var(--ink);
  }
  .intro__body p + p { margin-top: 19px; }

  /* Middle panel */
  .panel--guarantee { width: 362px; background: var(--panel-white); }
  .guarantee__title {
    position: absolute; left: 43px; top: 60px;
    font-family: "Bowlby One SC", sans-serif;
    font-size: 23px; font-weight: 400; color: var(--ink);
  }
  .guarantee__body {
    position: absolute; left: 43px; top: 91px; width: 312px;
    font-size: 19px; line-height: 29px; color: var(--ink);
  }
  .guarantee__body p + p { margin-top: 29px; }
  .guarantee__phone { color: var(--cyan); }
  .guarantee__ps {
    position: absolute; left: 14px; top: 656px;
    width: 331px; height: 168px;
    background: var(--cyan);
    padding: 14px 18px 0 34px;
    font-size: 15.5px; line-height: 20px; color: var(--ink);
    font-weight: 700;
  }
  .guarantee__ps-site { display: block; margin-top: 6px; font-size: 25px; font-weight: 400; }

  /* Right panel */
  .panel--cover { width: 364px; background: var(--panel-black); }
  .cover__strip { position: absolute; top: 0; height: 34px; }
  .cover__strip--grey { left: 0; width: 178px; background: var(--panel-grey); }
  .cover__strip--cyan { left: 178px; right: 0; background: var(--cyan); }
  .cover__headline {
    position: absolute; left: 30px; top: 112px; width: 330px;
    font-family: "Bowlby One SC", sans-serif;
    font-size: 29px; line-height: 34px; font-weight: 400;
    color: var(--white);
  }
  .cover__headline .accent { color: var(--cyan); }
  .cover__illustration {
    position: absolute; left: 22px; top: 416px; width: 300px; height: 252px;
    background: linear-gradient(120deg, var(--cyan) 0%, #3a3a3a 45%, var(--tan) 80%);
    opacity: .85;
    border-radius: 4px;
  }
  .cover__contact {
    position: absolute; left: 0; right: 0; top: 692px;
    text-align: center; color: var(--white);
  }
  .cover__contact-label { font-size: 19px; }
  .cover__contact-name { font-family: "Bowlby One SC", sans-serif; font-size: 21px; line-height: 26px; }
  .cover__contact-phone { font-family: "Bowlby One SC", sans-serif; font-size: 21px; line-height: 26px; color: var(--cyan); }
  .cover__site-band {
    position: absolute; left: 0; right: 0; top: 782px; height: 32px;
    background: var(--cyan);
    text-align: center;
    font-family: "Bowlby One SC", sans-serif;
    font-size: 21px; line-height: 32px; color: var(--white);
  }
</style>
</head>
<body>
  <main class="brochure">
    <section class="panel panel--intro">
      <svg class="intro__arrow" width="210" height="40" viewBox="0 0 210 40" aria-hidden="true">
        <path d="M6 26 C60 18 130 16 190 16" stroke="var(--cyan)" stroke-width="7" fill="none" stroke-linecap="round"/>
        <path d="M170 4 L204 16 L172 32" stroke="var(--cyan)" stroke-width="6" fill="none" stroke-linecap="round" stroke-linejoin="round"/>
      </svg>
      <div class="intro__site-vertical">TEMbexleyfold.com</div>
      <h2 class="intro__title">Are you tired of ineffective marketing and advertising?</h2>
      <div class="intro__body">
        <p>If you answered yes to either question, we should talk about our all-inclusive marketing plan. Our marketing plan places your menu in front of thousands of customers each and every month. Hungry customers looking to buy immediately. Hungry customers that want food now. The more views your menu receives, the more likely a customer will purchase food from your restaurant.</p>
        <p>Ever have a problem with down time at your restaurant? Customers are not dining in or taking out because it's too hot or too cold or it's raining outside? That's a problem that you wouldn't have to have, if you made your food more accessible.</p>
        <p>TEM Bexley Fold is a full service restaurant marketing and advertising service that specializes in delivery. We deliver food from a variety of restaurants to people at their homes, offices, and hotels! Using our marketing plan we will bring more exposure to your restaurant and increase your bottom line.</p>
      </div>
    </section>

    <section class="panel panel--guarantee">
      <h2 class="guarantee__title">We guarantee it!</h2>
      <div class="guarantee__body">
        <p>How many marketers and advertisers say that? We do! We guarantee that you will only make money and not pay money. There are never any participation cost, or fees associated with our service. We use a combination of 21 proven Marketing techniques to drive your profits up while keeping cost down.</p>
        <p>So what should you do? Call me now at <span class="guarantee__phone">555-014-2286</span> to schedule a 15 min consultation that is guaranteed to NOT cost you anything and only make your restaurant money.</p>
        <p>Talk to you soon!</p>
      </div>
      <div class="guarantee__ps">
        p.s.<br>
        I have a check with your restaurants name on it, so contact me before July 26, 2013! You can also schedule an appointment online at
        <span class="guarantee__ps-site">tembexleyfold.com</span>
      </div>
    </section>

    <section class="panel panel--cover">
      <div class="cover__strip cover__strip--grey"></div>
      <div class="cover__strip cover__strip--cyan"></div>
      <h1 class="cover__headline">Would <span class="accent">a check for $18,375 with your restaurants</span> name on it be worth a 15 min conversation?</h1>
      <div class="cover__illustration" role="img" aria-label="Brush-painted dollar signs in cyan, grey, white and tan"></div>
      <div class="cover__contact">
        <div class="cover__contact-label">Please talk to us :</div>
        <div class="cover__contact-name">Rowan Pell</div>
        <div class="cover__contact-phone">555-014-2286 (cell)</div>
      </div>
      <div class="cover__site-band">TEMbexleyfold.com</div>
    </section>
  </main>
</body>
</html>
```